Brochure Design Project (Design Studio)

Items required:
1-Brochure. We suggest 15Cm X 15 Cm after cutting.
2-Business Card.
3-Head letter.
4-Folder ( folder should carry the Brochure in pocket and the business card in a pocket on the opposite side of the folder.
5-Envelope to carry everything.
This brochure is expected to draw attention of high level management in companies to the quality and creativity of the design work and encourage them to do business with us. note that brochure will be printed in high quality printing and paper.
The game plan is as follows:
Over all description, the theme of the brochure is drawn from the website theme (website will be uploaded shortly, pictures of the website are attached, logo appears in the top left corner). Please avoid direct copying from the website unless it is a creative copying, just draw the theme from there. however, we need it to be elegant, stylish and class in colors and style. This is a MUST.
Furthermore, the main items of the Brochure:
1-The Studio is not just a studio: we will take about how Branding. A file is attached of the content. (slight changes/modification can apply during the designing process)
2-The Process: this one has to be a visual illustration of the process, it has to be very creative, could be elegant arrows and comics, could be elegant drawing, could be an elegant icons. The drawing should be separate from the steps, we need to the drawing and we need to have the steps listed and commentary, or if want to integrate both in one in an artistic way. Just don’t lose track of the theme and elegance. (steps and commentary are attached, slight changes/modification can apply at anytime.
3-Our Team: another drawing of your suggestion to illustrate the team members, we need to include the names and designation as well leave a place for some of them to say what they need to say about their style of designing. I leave it for your imagination to put this all together in a nice attractive visual illustration.
4-Works: this section will generally show the works of our designers. It needs to be focused on the works themselves, client should be able to view the details of the works ( note that when it comes to brochures and websites, we don’t need to reach to the extent with which the client can read the text in those pictures of the website or brochure, but still can see the overall design clearly). Each design is to carry the name of the designer. Last thing, this section will classify works into categories, like, Brochures, Corporate identity, print design. We didn’t finalize those categories, we will provide them to you shortly, last thing to be said, we are planning to include around 25-30 designs of each sub-category, eg. Corporate identity will have 30 business card s designs and 30 stationary designs.
5-Contacts: the company contacts.
We the brochure after printing should be 15x15 Cm.
Creativity and art work is a major player in selection.
general managers, owners
Printing

```html
<!DOCTYPE html>
<html lang="en">
<head>
<meta charset="utf-8">
<title>Branding</title>
<link href="https://fonts.googleapis.com/css2?family=Arimo:wght@400;700&display=swap" rel="stylesheet">
<style>
:root{
  --ink:#0c0c0c;
  --band:#5a5b5d;
  --band-dark:#262626;
  --text:#9c9c9c;
  --title:#dadada;
  --accent:#e10000;
  --rule:#6a6a6a;
}
*{margin:0;padding:0;box-sizing:border-box}
html,body{width:1200px;height:1200px;overflow:hidden;background:var(--ink)}
.page{position:relative;width:1200px;height:1200px;background:var(--ink);font-family:"Arimo",Arial,sans-serif;color:var(--text)}
.works{position:absolute;left:0;top:0;width:490px;height:1200px}
.work{position:absolute}
.band{position:absolute;top:0;left:490px;width:48px;height:1200px;background:var(--band)}
.band-inner{position:absolute;top:0;left:538px;width:24px;height:1200px;background:var(--band-dark)}
.copy{position:absolute;left:590px;width:576px}
.title{top:40px;font-size:27px;font-weight:700;color:var(--title);letter-spacing:.5px}
.rule{position:absolute;left:590px;width:576px;border-top:2px dotted var(--rule)}
.para{font-size:21px;line-height:27px;text-align:justify}
.dropcap{color:var(--accent);font-size:31px;font-weight:700}
.list-head{font-size:21px}
.list{position:absolute;left:693px;list-style:none;font-size:21px;line-height:27px}
.list li span{display:inline-block;width:37px}
.contact{position:absolute;right:53px;top:1155px;font-size:19px;color:var(--text);letter-spacing:-.8px}
.contact b{color:var(--title)}
</style>
</head>
<body>
<div class="page">
  <div class="works">
    <div class="work" role="img" aria-label="Bundle of brightly coloured printed pencils" style="left:0;top:0;width:258px;height:172px;background:linear-gradient(135deg,#e53a2e,#f2c31c 35%,#2a9bd8 60%,#5cc04a 80%,#222)"></div>
    <div class="work" role="img" aria-label="Brown pyramid coffee packaging with coffee beans" style="left:258px;top:0;width:232px;height:172px;background:linear-gradient(160deg,#8c8684,#5a2e26 60%,#3b1c16)"></div>
    <div class="work" role="img" aria-label="Black award-winning liner packaging box" style="left:0;top:172px;width:208px;height:208px;background:radial-gradient(circle at 55% 50%,#1a1a2a,#0b0b12 60%,#f2f2f2 62%)"></div>
    <div class="work" role="img" aria-label="Black square book with gold lettering on grey" style="left:208px;top:172px;width:282px;height:208px;background:linear-gradient(150deg,#e4e4e6,#b6b6bb 45%,#1a1a1a 46%,#0a0a0a 80%,#c9c9cc 81%)"></div>
    <div class="work" role="img" aria-label="Open furniture catalogue brochure on dark background" style="left:0;top:380px;width:326px;height:232px;background:linear-gradient(180deg,#0d0d0d 20%,#d8d6d2 35%,#efeeea 65%,#151515 80%)"></div>
    <div class="work" role="img" aria-label="Black die-cut booklets with leaf silhouettes on white" style="left:326px;top:380px;width:164px;height:232px;background:radial-gradient(circle at 55% 50%,#1c1c1c 30%,#f7f7f7 60%)"></div>
    <div class="work" role="img" aria-label="Colourful liner pouches in a tin case" style="left:0;top:612px;width:200px;height:198px;background:linear-gradient(120deg,#fff 25%,#f0e020 40%,#e83c98 55%,#2da7e0 70%,#9ad020 85%,#fff)"></div>
    <div class="work" role="img" aria-label="White folded brochure stack on dark grey" style="left:200px;top:612px;width:290px;height:198px;background:radial-gradient(ellipse at 50% 60%,#d9d7d0 30%,#2b2b2b 60%,#111)"></div>
    <div class="work" role="img" aria-label="Light bulb poster filled with water for an energy campaign" style="left:0;top:810px;width:202px;height:254px;background:radial-gradient(ellipse at 50% 40%,#9a9a9a,#2a2a2a 40%,#000 70%)"></div>
    <div class="work" role="img" aria-label="Red museum folder on white background" style="left:202px;top:810px;width:288px;height:188px;background:linear-gradient(160deg,#f4f4f4 20%,#d8121a 35%,#b80c12 75%,#f4f4f4 90%)"></div>
    <div class="work" role="img" aria-label="Dark invitation card with green circle illustration" style="left:0;top:1064px;width:202px;height:136px;background:radial-gradient(circle at 55% 50%,#8ad82a 15%,#3a3030 35%,#1a1818)"></div>
    <div class="work" role="img" aria-label="Collage of colourful brochures and typographic print pieces" style="left:202px;top:998px;width:288px;height:202px;background:linear-gradient(135deg,#e4e4e4 20%,#c8242c 40%,#1a1a1a 60%,#2a8fd0 80%,#e7c23a)"></div>
  </div>
  <div class="band"></div>
  <div class="band-inner"></div>

  <h1 class="copy title">BRANDING</h1>
  <div class="rule" style="top:83px"></div>

  <p class="copy para" style="top:114px"><span class="dropcap">D</span>o you prefer to work with specific Individuals over others? Do you feel that working with those individuals give you the peace of mind because you know that they are Enthusiastic, ethical, Goal Focused, Committed, Disciplined, creative, visionary and self-aware?</p>

  <p class="copy para" style="top:284px">Well, probably you like to work with companies of the same qualities as those persons! COMPANIES HAVE PERSONALITIES TOO.</p>

  <p class="copy para" style="top:392px">Branding is your vehicle to deliver the traits of your company to the audience. Branding assist you to control the perception of company among public.<br>If you are very organized company, deliver on time, committed to your clients, produce quality products to the highest standards. Branding is the key to make the public hear and believe those qualities and consider your products as their 1st choice.</p>

  <p class="copy list-head" style="top:672px">Strong Branding Means you company is:</p>
  <ol class="list" style="top:715px">
    <li><span>1.</span>Large and established.</li>
    <li><span>2.</span>A synonym of Quality.</li>
    <li><span>3.</span>Experienced and reliable.</li>
  </ol>

  <p class="copy list-head" style="top:851px">Branding gives you:</p>
  <ol class="list" style="top:893px">
    <li><span>1.</span>Loyalty and advocacy.</li>
    <li><span>2.</span>Influence of choice.</li>
    <li><span>3.</span>Command a price premium.</li>
    <li><span>4.</span>Uniqueness.</li>
    <li><span>5.</span>Growth of your business and products.</li>
  </ol>

  <div class="rule" style="top:1130px"></div>
  <p class="contact">Contact Us: <b>00 971 2 555 0192</b></p>
</div>
</body>
</html>
```